Update our OBGYN business card look and info

We are an OBGYN office. Our logo is nice but would like to "woman" part of the logo to be a darker color, to contrast with the flower that surrounds it. Maybe make our practice name Bloom Circle Health more feminine. Our practice caters to women only. All providers and staff are female.

Target Market(s)

Females 16-65.

Industry/Entity Type

Business

Contact Information for Business Card

See attached upload. The ONLY CHANGE to the information is DELETE the name Marla Quenbright, Midwife and REPLACE with Tessa Dravinoux, Midwife

Logo Text

Bloom Circle Health Obstetrics & Gynecology

Font styles to use
Serif
Script

Colors
85cae6
0692cd
33a6d7
85abd2
f59195
eea4c8
cadf82
fac994
d3a5cc

```html
<!DOCTYPE html>
<html lang="en">
<head>
<meta charset="utf-8">
<title>Bloom Circle Health – Business Card</title>
<link rel="stylesheet" href="https://fonts.googleapis.com/css2?family=Tinos:wght@400;700&display=swap">
<style>
  :root {
    --page-bg: #e9e4dc;
    --card-white: #fbfbfb;
    --pink: #f0a3a8;
    --pink-text: #ec8f97;
    --blue-light: #14c0e4;
    --blue-mid: #33a6d7;
    --blue-deep: #0692cd;
    --back-light: #7ccbe6;
    --back-dark: #2f82bb;
    --white: #ffffff;
  }
  * { box-sizing: border-box; margin: 0; padding: 0; }
  html, body { width: 1200px; height: 780px; overflow: hidden; }
  body {
    background: var(--page-bg);
    font-family: "Tinos", "Times New Roman", serif;
    display: flex;
    align-items: center;
    justify-content: center;
    gap: 40px;
  }
  .card {
    position: relative;
    width: 540px;
    height: 308px;
    border-radius: 18px;
    overflow: hidden;
    box-shadow: 0 10px 28px rgba(0,0,0,.18);
  }
  .card-front { background: var(--card-white); }
  .card-bg { position: absolute; inset: 0; width: 100%; height: 100%; }

  .brand {
    position: absolute;
    left: 30px;
    top: 58px;
  }
  .brand-name {
    display: flex;
    align-items: center;
    gap: 10px;
    font-size: 30px;
    color: var(--pink-text);
    font-weight: 400;
    line-height: 1;
    white-space: nowrap;
  }
  .brand-dot {
    width: 30px; height: 30px;
    border-radius: 50%;
    background: var(--blue-mid);
    flex: none;
  }
  .brand-tagline {
    margin: 8px 0 0 40px;
    font-size: 12.5px;
    letter-spacing: 1.5px;
    text-transform: uppercase;
    color: var(--pink-text);
    white-space: nowrap;
  }

  .address {
    position: absolute;
    right: 112px;
    top: 16px;
    text-align: right;
    font-style: normal;
    font-size: 13px;
    line-height: 1.35;
    color: var(--blue-mid);
    white-space: nowrap;
  }

  .providers {
    position: absolute;
    left: 110px;
    bottom: 14px;
    list-style: none;
    color: var(--white);
    font-size: 13px;
    line-height: 1.3;
    white-space: nowrap;
  }

  .contact {
    position: absolute;
    right: 26px;
    top: 146px;
    list-style: none;
    color: var(--white);
    font-size: 13px;
    line-height: 1;
    white-space: nowrap;
  }
  .contact li { display: flex; align-items: center; gap: 7px; margin-bottom: 7px; }
  .contact-icon {
    width: 15px; height: 15px;
    border-radius: 50%;
    border: 1.2px solid var(--white);
    display: flex; align-items: center; justify-content: center;
    flex: none;
  }
  .contact-icon svg { width: 9px; height: 9px; }

  .card-back {
    background: radial-gradient(ellipse at 50% 50%, var(--back-light) 0%, #4aa4d2 45%, var(--back-dark) 100%);
    display: flex;
    flex-direction: column;
    align-items: center;
    justify-content: center;
    gap: 16px;
    color: var(--white);
  }
  .back-brand {
    display: flex;
    align-items: center;
    gap: 12px;
    font-size: 30px;
    color: var(--white);
  }
  .back-dot {
    width: 30px; height: 30px;
    border-radius: 50%;
    background: var(--white);
  }
  .back-web { font-size: 14px; letter-spacing: 1px; }
</style>
</head>
<body>

  <section class="card card-front" aria-label="Business card front">
    <svg class="card-bg" viewBox="0 0 540 308" preserveAspectRatio="none" aria-hidden="true">
      <defs>
        <linearGradient id="frontBlue" x1="0" y1="0" x2="1" y2="1">
          <stop offset="0" stop-color="#14c3e6"/>
          <stop offset="1" stop-color="#0692cd"/>
        </linearGradient>
      </defs>
      <path class="pink-band" fill="#f0a3a8"
            d="M0 200 C 180 190, 300 165, 380 115 S 480 20 540 14 L 540 308 L 0 308 Z"/>
      <path class="white-gap" fill="#fbfbfb" transform="translate(0 9)"
            d="M0 200 C 180 190, 300 165, 380 115 S 480 20 540 14 L 540 308 L 0 308 Z"/>
      <path class="blue-field" fill="url(#frontBlue)" transform="translate(0 13)"
            d="M0 200 C 180 190, 300 165, 380 115 S 480 20 540 14 L 540 308 L 0 308 Z"/>
    </svg>

    <div class="brand">
      <div class="brand-name"><span class="brand-dot"></span>Bloom Circle Health</div>
      <div class="brand-tagline">Obstetrics &amp; Gynecology</div>
    </div>

    <address class="address">
      418 Larkspur Ave, Ste 3B<br>
      Fairhaven, GA 30999-0142
    </address>

    <ul class="providers">
      <li>Renata Calloway, MD</li>
      <li>Dana Whitcombe, MD</li>
      <li>Ilse Moravec, MD</li>
      <li>Priya Stennard, Midwife</li>
      <li>Tessa Dravinoux, Midwife</li>
    </ul>

    <ul class="contact">
      <li>
        <span class="contact-icon">
          <svg viewBox="0 0 10 10"><path d="M2 1 L4 1 L4.5 3 L3.3 3.8 Q4.3 5.8 6.2 6.7 L7 5.5 L9 6 L9 8 Q5 9 2.5 6.5 Q0.5 4 2 1 Z" fill="#fff"/></svg>
        </span>
        555-201-4830
      </li>
      <li>
        <span class="contact-icon">
          <svg viewBox="0 0 10 10"><rect x="1" y="4" width="8" height="4.5" rx="0.8" fill="#fff"/><rect x="2.8" y="1.2" width="4.4" height="3" fill="none" stroke="#fff" stroke-width="1"/></svg>
        </span>
        555-201-4917
      </li>
      <li>
        <span class="contact-icon">
          <svg viewBox="0 0 10 10"><circle cx="5" cy="5" r="4" fill="none" stroke="#fff" stroke-width="0.9"/><ellipse cx="5" cy="5" rx="1.8" ry="4" fill="none" stroke="#fff" stroke-width="0.8"/><line x1="1" y1="5" x2="9" y2="5" stroke="#fff" stroke-width="0.8"/></svg>
        </span>
        www.bloomcirclehealth.com
      </li>
    </ul>
  </section>

  <section class="card card-back" aria-label="Business card back">
    <div class="back-brand"><span class="back-dot"></span>Bloom Circle Health</div>
    <div class="back-web">www.bloomcirclehealth.com</div>
  </section>

</body>
</html>
```